Harbour Fellows - community/social/support group for men needs a flyer

We need a flyer for our community group for display in GP clinics and other community services offices. Please refer to our website for design ideas: www.harbourfellows.org.au. We need it to be clean and simple to read.

Target Market(s)

Men 18+

Font styles to use
Serif

Colors
00a990

```html
<!DOCTYPE html>
<html lang="en">
<head>
<meta charset="utf-8">
<title>Harbour Fellows – Flyer</title>
<link href="https://fonts.googleapis.com/css2?family=Playfair+Display:wght@900&family=PT+Serif:wght@400;700&display=swap" rel="stylesheet">
<style>
  :root {
    --brand-teal: #00a990;
    --brand-teal-dark: #00806d;
    --ink: #1d1d1b;
    --paper: #ffffff;
    --photo-light: #3fbfa9;
    --photo-mid: #169a85;
    --photo-deep: #135a52;
    --photo-green: #3f6a4c;
  }
  * { margin: 0; padding: 0; box-sizing: border-box; }
  html, body { width: 849px; height: 1200px; overflow: hidden; background: var(--paper); }
  .flyer {
    position: relative; width: 849px; height: 1200px; overflow: hidden;
    background: var(--paper); font-family: "PT Serif", Georgia, serif; color: var(--ink);
  }
  .top-band { position: absolute; left: 0; top: 0; }
  .brand-mark { position: absolute; top: 22px; left: 0; width: 849px; text-align: center; }
  .brand-mark__square {
    display: block; width: 20px; height: 20px; margin: 0 auto 14px; background: var(--ink);
  }
  .brand-mark__name {
    font-family: "PT Serif", Georgia, serif; font-weight: 700; font-size: 22px;
    letter-spacing: 1px; color: var(--ink);
  }
  .hero { position: absolute; left: 0; top: 0; }
  .tagline {
    position: absolute; top: 478px; left: 0; width: 849px; text-align: center;
    color: var(--paper); font-size: 24px; line-height: 30px;
    text-shadow: 0 1px 3px rgba(0,0,0,0.25);
  }
  .about {
    position: absolute; left: 32px; top: 772px; width: 363px;
    font-size: 15.5px; line-height: 20.5px; text-align: justify; hyphens: manual;
  }
  .divider {
    position: absolute; left: 424px; top: 773px; width: 1.5px; height: 240px;
    background: var(--brand-teal);
  }
  .projects { position: absolute; left: 459px; top: 768px; width: 370px; }
  .projects__heading {
    color: var(--brand-teal); font-weight: 700; font-size: 18px; line-height: 23.5px;
  }
  .projects__list { list-style: none; margin-top: 14px; }
  .projects__list li {
    position: relative; padding-left: 23px; font-size: 15.5px; line-height: 24.6px;
  }
  .projects__list li::before {
    content: ""; position: absolute; left: 0; top: 8px; width: 10px; height: 10px;
    border-radius: 50%; background: var(--brand-teal);
  }
  .projects__list li.plain::before { display: none; }
  .footer {
    position: absolute; left: 0; top: 1061px; width: 849px; height: 139px;
    background: var(--brand-teal); color: var(--paper); text-align: center;
  }
  .footer__lead { margin-top: 22px; font-weight: 700; font-size: 14.5px; }
  .footer__url { margin-top: 4px; font-weight: 700; font-size: 35px; line-height: 42px; }
  .footer__social { margin-top: 2px; font-weight: 700; font-size: 17px; }
</style>
</head>
<body>
<div class="flyer">

  <svg class="top-band" width="849" height="22" viewBox="0 0 849 22">
    <polygon fill="var(--brand-teal)" points="0,0 849,0 849,20 515,20 497,2 353,2 335,20 0,20"/>
  </svg>

  <div class="brand-mark">
    <span class="brand-mark__square"></span>
    <span class="brand-mark__name">HARBOUR FELLOWS</span>
  </div>

  <svg class="hero" width="849" height="760" viewBox="0 0 849 760">
    <defs>
      <linearGradient id="photoSide" x1="0" y1="0" x2="1" y2="1">
        <stop offset="0" stop-color="var(--photo-light)"/>
        <stop offset="1" stop-color="var(--photo-mid)"/>
      </linearGradient>
      <linearGradient id="photoCentre" x1="0" y1="0" x2="0" y2="1">
        <stop offset="0" stop-color="var(--photo-green)"/>
        <stop offset="0.45" stop-color="#2d6f63"/>
        <stop offset="1" stop-color="var(--photo-mid)"/>
      </linearGradient>
      <linearGradient id="photoSmall" x1="0" y1="0" x2="1" y2="1">
        <stop offset="0" stop-color="#4f8a7c"/>
        <stop offset="1" stop-color="var(--photo-deep)"/>
      </linearGradient>
    </defs>
    <g role="img" aria-label="Photo collage of a group of laughing friends outdoors, arms around each other, in teal tones">
      <polygon fill="url(#photoSide)" points="0,130 183,313 100,403 0,490"/>
      <polygon fill="url(#photoSide)" points="0,505 94,420 183,507 0,692"/>
      <polygon fill="url(#photoSide)" points="849,130 666,313 745,403 849,318"/>
      <polygon fill="url(#photoSide)" points="849,336 755,418 666,507 849,692"/>
      <path fill="url(#photoSmall)" d="M200.7 88 L300 185 Q306 191 300 197 L206 290 Q200.7 296 195 290 L101 197 Q95 191 101 185 Z"/>
      <path fill="url(#photoSmall)" d="M648 88 L747 185 Q753 191 747 197 L653 290 Q648 296 642 290 L548 197 Q542 191 548 185 Z"/>
      <path fill="url(#photoSmall)" d="M200.7 534 L300 631 Q306 637 300 643 L206 736 Q200.7 742 195 736 L101 643 Q95 637 101 631 Z"/>
      <path fill="url(#photoSmall)" d="M648 534 L747 631 Q753 637 747 643 L653 736 Q648 742 642 736 L548 643 Q542 637 548 631 Z"/>
      <path fill="url(#photoCentre)" d="M424.5 116 L717 407 Q724 413 717 419 L430.5 705 Q424.5 711 418.5 705 L132 419 Q125 413 132 407 L418.5 122 Z"/>
    </g>
    <polyline fill="none" stroke="var(--brand-teal)" stroke-width="2" points="207,375 605,375 663,319"/>
    <polyline fill="none" stroke="var(--brand-teal)" stroke-width="2" points="642,463 230,463 186,506"/>
    <text x="424.5" y="447" text-anchor="middle" textLength="434" lengthAdjust="spacingAndGlyphs"
          font-family="'Playfair Display', Georgia, serif" font-weight="900" font-size="66" fill="#ffffff">HARBOUR FELLOWS</text>
  </svg>

  <p class="tagline">Social. Support.<br>Mateship. Community.</p>

  <p class="about">Harbour Fellows Inc. is a community group that supports the positive activity, engagement and inclusion of men in Kellerton's Ashvale Ranges. Our aim is to reduce the number of men who are socially disadvantaged, marginalised or isolated to become productive, active members of the local community. We do this by providing opportunities for men (18 years+) to come together in open, non-judgemental, safe spaces and participate in a range of social activities that encourage new friendships, normalise help-seeking behaviours and link with local support services.</p>

  <div class="divider"></div>

  <section class="projects">
    <h2 class="projects__heading">We run a number of projects each year, which currently include:</h2>
    <ul class="projects__list">
      <li>Dads and kids playgroup;</li>
      <li>Games Night;</li>
      <li>Yarning Circle (men's discussion group);</li>
      <li>GBTIQ+ social dinners;</li>
      <li>Shared Services working bee's;</li>
      <li>Guest speakers;</li>
      <li>Annual men's gathering</li>
      <li class="plain">And more.</li>
    </ul>
  </section>

  <footer class="footer">
    <p class="footer__lead">For a list of our current activities and to find our how you can get involved, please visit us online at:</p>
    <p class="footer__url">www.HarbourFellows.org.au</p>
    <p class="footer__social">www.friendspace.com/harbourfellowsAU/</p>
  </footer>

</div>
</body>
</html>
```